Velmora Car Care glossy Brochure

i would like a brochure designed that describes our various package and extras that we provide.
i have uploaded an example of the style of brochure i am looking for. The brochure must be in a trifold format.

Target Market(s)

Car lovers and anybody that cares about their car. busy professionals that don't have time to clean their car.

Industry/Entity Type

Car cleaning and detailing sector

Font styles to use
Other font styles liked:
• impact or similar

Requirements
Must have
• Detail Packages and any images of a 2017 Krandel Toriva ute. use image that i have uploaded as well.
Nice to have
• Same vibe as my other company material. I have uploaded some images of me buffing etc, use me in the brochure as an image with feathered edges. I have also uploaded my logo.⁸⁹⁸

```html
<!DOCTYPE html>
<html lang="en">
<head>
<meta charset="utf-8">
<title>Velmora Car Care – Detailing Packages</title>
<link href="https://fonts.googleapis.com/css2?family=Anton&family=Open+Sans:wght@400;600;700;800&display=swap" rel="stylesheet">
<style>
:root{
  --page:#9a9a9a;
  --black:#060606;
  --gold:#c9a24a;
  --gold-light:#e6c877;
  --gold-dark:#8a6a25;
  --white:#ffffff;
  --text:#f2f2f2;
}
*{box-sizing:border-box;margin:0;padding:0}
html,body{width:857px;height:1200px;overflow:hidden;background:var(--page)}
.stage{position:relative;width:857px;height:1200px}
.flyer{
  position:absolute;left:20px;top:311px;width:1207px;height:853px;
  transform:scale(0.6769);transform-origin:0 0;overflow:hidden;
  background:radial-gradient(ellipse at 50% 40%,#1a1a1a 0%,var(--black) 70%);
  font-family:"Open Sans",Arial,sans-serif;color:var(--text);
  box-shadow:0 6px 18px rgba(0,0,0,.35);
}
.abs{position:absolute}
.fold{top:0;width:0;height:853px;border-left:1px dashed rgba(255,255,255,.12);z-index:5}
.fold-1{left:402px}.fold-2{left:805px}
.hero-ring{left:0;top:0}
.title{left:0;width:1207px;text-align:center;font-family:"Anton",Impact,sans-serif;line-height:1;letter-spacing:1px}
.title-top{top:34px;font-size:76px;color:var(--white)}
.title-bottom{top:104px;font-size:76px;color:var(--gold)}
.brand{left:60px;top:112px;display:flex;align-items:center;gap:14px}
.brand-dot{width:70px;height:70px;border-radius:50%;background:var(--gold)}
.brand-name{font-family:"Anton",Impact,sans-serif;font-size:40px;line-height:1.05;color:var(--gold)}
.photo-detailer{
  left:850px;top:18px;width:357px;height:300px;
  background:linear-gradient(90deg,rgba(6,6,6,0) 0%,#3a3a3a 22%,#d9d9d9 70%,#f4f4f4 100%);
  -webkit-mask-image:radial-gradient(ellipse at 65% 50%,#000 55%,transparent 80%);
          mask-image:radial-gradient(ellipse at 65% 50%,#000 55%,transparent 80%);
}
.values{top:329px;left:0;width:1207px;text-align:center;font-size:13.5px;font-weight:700;color:var(--white);letter-spacing:.2px}
.values .sep{color:var(--gold);margin:0 8px}
.package{top:370px;width:368px;height:228px;border:2px solid var(--gold);border-radius:8px;
  background:linear-gradient(180deg,#1b1b1b,#0b0b0b);overflow:hidden}
.package-1{left:36px}.package-2{left:421px}.package-3{left:805px}
.package-tab{position:absolute;left:24px;top:-2px;width:140px;height:24px;background:var(--gold);
  color:#111;font-weight:800;font-size:13px;text-align:center;line-height:24px;letter-spacing:.4px}
.package-from{position:absolute;right:24px;top:5px;font-size:11px;letter-spacing:2px;color:var(--gold)}
.package-title{position:absolute;left:22px;top:28px;font-family:"Anton",Impact,sans-serif;font-weight:400;font-size:25px;color:var(--gold);letter-spacing:.3px}
.package-price{position:absolute;right:22px;top:18px;font-family:"Anton",Impact,sans-serif;font-size:40px;color:var(--white);font-style:italic}
.package-rule{position:absolute;left:10px;right:10px;top:72px;height:1px;background:#555}
.package-list{position:absolute;left:0;right:0;top:78px;list-style:none;text-align:center;font-size:14px;color:var(--white)}
.package-1 .package-list{top:90px}
.package-list li{height:24px;line-height:24px;border-bottom:1px solid #262626;margin:0 20px}
.package-list li:last-child{border-bottom:0}
.package-corner{position:absolute;right:0;bottom:0}
.badge-popular{position:absolute;left:14px;top:150px;width:64px;height:64px;border-radius:50%;
  background:radial-gradient(circle,var(--gold-light),var(--gold-dark));border:2px dashed #6b5020;
  color:#1a1a1a;font-family:"Anton",Impact,sans-serif;font-size:13px;line-height:1.05;text-align:center;
  padding-top:17px;transform:rotate(-12deg)}
.addons-heading{top:622px;left:408px;width:735px;display:flex;align-items:center;gap:10px}
.addons-heading .line{flex:1;height:2px;background:var(--gold)}
.addons-heading span{font-family:"Anton",Impact,sans-serif;font-size:19px;color:var(--gold)}
.photo-van{left:28px;top:640px;width:330px;height:175px;border-radius:40px 60px 20px 20px;
  background:linear-gradient(120deg,#1c1c1c 0%,#2b2b2b 40%,#b08a3a 60%,#1c1c1c 100%)}
.addon{top:658px;display:flex;align-items:center;gap:8px}
.addon-icon{width:24px;height:24px;flex:none}
.addon-label{font-size:13px;font-weight:700;line-height:1.25;color:var(--white)}
.addon-price{text-align:center;margin-left:8px}
.addon-price small{display:block;font-size:11px;letter-spacing:2px;color:var(--text)}
.addon-price b{display:inline-block;border:1.5px solid var(--gold);border-radius:5px;padding:0 8px;
  font-family:"Anton",Impact,sans-serif;font-weight:400;font-size:20px;color:var(--gold)}
.addon-divider{top:664px;width:1px;height:40px;background:#555}
.call-band{left:353px;top:733px;width:854px;height:50px;
  background:linear-gradient(90deg,#fff 0%,#fff 52%,#e8d39c 68%,var(--gold) 80%,var(--gold-dark) 100%);
  clip-path:polygon(0 10%,4% 0,60% 4%,100% 0,100% 100%,50% 96%,3% 100%,1% 86%)}
.call-text{left:424px;top:738px;display:flex;align-items:center;gap:8px;font-family:"Anton",Impact,sans-serif;color:#111}
.call-text .lead{font-size:26px}
.call-text .num{font-size:34px}
.touch{left:930px;top:743px;display:flex;align-items:center;gap:8px;font-weight:800;font-size:19px;color:#111}
.touch i{display:inline-block;width:28px;height:28px;border-radius:50%;background:#111}
.slogan{top:803px;left:0;width:1207px;text-align:center;font-weight:800;font-size:19px;letter-spacing:5px}
.slogan .g{color:var(--gold)}
</style>
</head>
<body>
<div class="stage">
  <div class="flyer">
    <svg class="abs hero-ring" width="1207" height="330" viewBox="0 0 1207 330">
      <defs>
        <linearGradient id="goldGrad" x1="0" y1="0" x2="1" y2="1">
          <stop offset="0" stop-color="#e6c877"/><stop offset=".5" stop-color="#b8862f"/><stop offset="1" stop-color="#e6c877"/>
        </linearGradient>
        <path id="arcText" d="M 377.5 192.3 A 293 293 0 0 0 826.5 192.3"/>
      </defs>
      <circle cx="602" cy="4" r="310" fill="none" stroke="url(#goldGrad)" stroke-width="6"/>
      <circle cx="602" cy="4" r="302" fill="#fff"/>
      <circle cx="602" cy="4" r="276" fill="#0d0d0d"/>
      <text font-family="Open Sans, sans-serif" font-weight="700" font-size="15" letter-spacing="1">
        <textPath href="#arcText" startOffset="50%" text-anchor="middle"><tspan fill="#b8892f">MOBILE CAR DETAILING</tspan><tspan fill="#111"> - WE COME TO YOU!</tspan></textPath>
      </text>
    </svg>
    <div class="abs title title-top">DETAILING</div>
    <div class="abs title title-bottom">PACKAGES</div>

    <div class="abs brand"><div class="brand-dot"></div><div class="brand-name">Velmora<br>Car Care</div></div>

    <div class="abs photo-detailer" role="img" aria-label="Detailer kneeling and buffing a white ute with a yellow microfibre cloth"></div>

    <div class="abs values">PREMIUM PRODUCTS<span class="sep">|</span>ATTENTION TO DEAL<span class="sep">|</span>RELABLE &amp; ON TIME<span class="sep">|</span>100% SATISFACTION GUARANTEE<span class="sep">|</span>CAIRNS &amp; SURROUNDS</div>

    <section class="abs package package-1">
      <div class="package-tab">PACKAGE 1</div><div class="package-from">FROM</div>
      <h2 class="package-title">BASIC WASH</h2><div class="package-price">$99</div><div class="package-rule"></div>
      <ul class="package-list"><li>Exterior wash &amp; rinse</li><li>Wheels cleaned</li><li>Tyre shine</li><li>Windows cleaned</li><li>Quick interior vacuum</li></ul>
      <svg class="package-corner" width="130" height="110" viewBox="0 0 130 110"><path d="M130 0 Q110 85 0 110 L130 110Z" fill="url(#goldGrad)"/><path d="M104 80 q8 10 8 16 a8 8 0 0 1-16 0 q0-6 8-16z" fill="#111"/></svg>
    </section>
    <section class="abs package package-2">
      <div class="package-tab">PACKAGE 2</div><div class="package-from">FROM</div>
      <h2 class="package-title">FULL DETAIL</h2><div class="package-price">$199</div><div class="package-rule"></div>
      <ul class="package-list"><li>Everything in Basic Wash</li><li>Full interior vacuum</li><li>Dash, console &amp; trims wiped clean</li><li>Door jambs cleaned</li><li>Exterior hand dry</li><li>Spray sealant protection</li></ul>
      <div class="badge-popular">MOST<br>POPULAR</div>
      <svg class="package-corner" width="130" height="110" viewBox="0 0 130 110"><path d="M130 0 Q110 85 0 110 L130 110Z" fill="url(#goldGrad)"/><path d="M104 78 l10 4 v8 q0 9-10 13 q-10-4-10-13 v-8z" fill="#111"/></svg>
    </section>
    <section class="abs package package-3">
      <div class="package-tab">PACKAGE 3</div><div class="package-from">FROM</div>
      <h2 class="package-title">PREMIUM DETAIL</h2><div class="package-price">$349</div><div class="package-rule"></div>
      <ul class="package-list"><li>Everything in Full Detail</li><li>Paint decontamination</li><li>Machine polish (light correction)</li><li>Interior deep clean</li><li>Trim restoration</li><li>High gloss finish</li></ul>
      <svg class="package-corner" width="130" height="110" viewBox="0 0 130 110"><path d="M130 0 Q110 85 0 110 L130 110Z" fill="url(#goldGrad)"/><path d="M94 84 l6 6 l5-9 l5 9 l6-6 l-2 14 h-18z" fill="#111"/></svg>
    </section>

    <div class="abs addons-heading"><div class="line"></div><span>POPULAR ADD-ONS</span><div class="line"></div></div>

    <div class="abs photo-van" role="img" aria-label="Black and gold wrapped service van"></div>

    <div class="abs addon" style="left:358px">
      <svg class="addon-icon" viewBox="0 0 24 24"><circle cx="12" cy="12" r="8" fill="none" stroke="#c9a24a" stroke-width="3"/><circle cx="12" cy="12" r="3" fill="#c9a24a"/></svg>
      <div class="addon-label">ENGINE BAY<br>DETAIL</div>
      <div class="addon-price"><small>FROM</small><b>$599</b></div>
    </div>
    <div class="abs addon-divider" style="left:550px"></div>
    <div class="abs addon" style="left:558px">
      <svg class="addon-icon" viewBox="0 0 24 24"><path d="M12 2 l9 4 v6 q0 7-9 10 q-9-3-9-10 v-6z" fill="none" stroke="#c9a24a" stroke-width="2.5"/></svg>
      <div class="addon-label">CERAMIC<br>COATING</div>
      <div class="addon-price"><small>FROM</small><b>$599</b></div>
    </div>
    <div class="abs addon-divider" style="left:738px"></div>
    <div class="abs addon" style="left:746px">
      <svg class="addon-icon" viewBox="0 0 24 24" fill="#c9a24a"><ellipse cx="12" cy="16" rx="6" ry="5"/><circle cx="5" cy="9" r="2.5"/><circle cx="10" cy="5" r="2.5"/><circle cx="15" cy="5" r="2.5"/><circle cx="20" cy="9" r="2.5"/></svg>
      <div class="addon-label">PET HAIR<br>REMOVAL</div>
      <div class="addon-price"><small>FROM</small><b>$50-$100</b></div>
    </div>
    <div class="abs addon-divider" style="left:955px"></div>
    <div class="abs addon" style="left:962px">
      <svg class="addon-icon" viewBox="0 0 24 24"><path d="M10 4 q-8 8 0 16z" fill="#c9a24a"/><path d="M14 7 h8 M14 12 h8 M14 17 h8" stroke="#c9a24a" stroke-width="2.5"/></svg>
      <div class="addon-label">HEADLIGHT<br>RESTORATION</div>
      <div class="addon-price" style="margin-left:20px"><small>FROM</small><b>$80</b></div>
    </div>

    <div class="abs call-band"></div>
    <div class="abs call-text">
      <span class="lead">CALL US NOW!</span>
      <svg width="30" height="30" viewBox="0 0 30 30"><circle cx="15" cy="15" r="14" fill="#111"/><path d="M10 8 l3 0 l1.5 4 l-2 1.5 q1.5 3.5 4 5 l1.5-2 l4 1.5 v3 q-1 1.5-3 1.5 q-10-2-11-12 q0-1.5 2-2.5z" fill="#fff"/></svg>
      <span class="num">0400 555 182</span>
    </div>
    <div class="abs touch">Get in Touch <i></i><i></i></div>

    <div class="abs slogan"><span class="g">PROFESSIONAL</span> CARE. <span class="g">PREMIUM</span> RESULTS.</div>

    <div class="abs fold fold-1" aria-hidden="true"></div>
    <div class="abs fold fold-2" aria-hidden="true"></div>
  </div>
</div>
</body>
</html>
```